Email Signatures

I would like to create a new email signature for my team. The design will be the same for everyone, with only individual details such as name and email changing. You can also see our brand style on our website. https://www.tlmbespokehomes.com.au/

Target Market(s)

Clients for new builds or renovations

Industry/Entity Type

Construction

Colors

Designer to choose colors to be used in the design.

```html
<!DOCTYPE html>
<html lang="en">
<head>
<meta charset="utf-8">
<title>TLM Bespoke Homes — Email Signature</title>
<link href="https://fonts.googleapis.com/css2?family=Montserrat:ital,wght@0,500;0,700;1,400&family=Poppins:wght@400;500&display=swap" rel="stylesheet">
<style>
  :root {
    --green: #4caf48;
    --black: #1b1b1b;
    --paper: #f3f4f6;
    --band-grey: #d3d3d3;
    --frame-white: #f2f2f2;
    --photo-grey: #5f5f5f;
    --white: #ffffff;
  }
  html, body { margin: 0; padding: 0; overflow: hidden; background: var(--paper); }
  .signature {
    position: relative;
    width: 1200px;
    height: 400px;
    overflow: hidden;
    background: var(--paper);
    font-family: "Montserrat", Arial, sans-serif;
  }
  .signature__art { position: absolute; inset: 0; }
  .brand {
    position: absolute;
    left: 62px;
    top: 34px;
    width: 150px;
    color: var(--white);
    font-weight: 700;
    font-size: 17px;
    line-height: 1.15;
    letter-spacing: 0.5px;
    display: flex;
    align-items: center;
    gap: 8px;
  }
  .brand__mark { width: 12px; height: 12px; background: var(--green); flex: none; }
  .portrait-label {
    position: absolute;
    left: 280px;
    top: 166px;
    width: 120px;
    text-align: center;
    color: #e6e6e6;
    font-family: "Poppins", Arial, sans-serif;
    font-size: 38px;
  }
  .person-name {
    position: absolute;
    left: 693px;
    top: 78px;
    margin: 0;
    color: var(--white);
    font-weight: 700;
    font-size: 29px;
    letter-spacing: 0.3px;
  }
  .person-role {
    position: absolute;
    left: 693px;
    top: 149px;
    margin: 0;
    color: var(--white);
    font-weight: 500;
    font-size: 21px;
  }
  .contact {
    position: absolute;
    top: 234px;
    display: flex;
    align-items: center;
    gap: 12px;
    font-family: "Poppins", Arial, sans-serif;
    font-weight: 500;
    font-size: 26px;
    color: var(--black);
    letter-spacing: 0.5px;
  }
  .contact--phone { left: 607px; }
  .contact--email { left: 893px; }
  .contact__icon { width: 42px; height: 42px; }
  .website {
    position: absolute;
    left: 600px;
    width: 600px;
    top: 344px;
    text-align: center;
    color: var(--white);
    font-style: italic;
    font-weight: 400;
    font-size: 23px;
  }
</style>
</head>
<body>
<div class="signature">
  <svg class="signature__art" width="1200" height="400" viewBox="0 0 1200 400" aria-hidden="false">
    <defs>
      <linearGradient id="photoTones" x1="0" y1="0" x2="1" y2="1">
        <stop offset="0" stop-color="#4a4f57"/>
        <stop offset="0.45" stop-color="#8b8f95"/>
        <stop offset="0.75" stop-color="#6b5a4a"/>
        <stop offset="1" stop-color="#c9c4bb"/>
      </linearGradient>
    </defs>
    <!-- project imagery -->
    <polygon class="project-photos" role="img" aria-label="Photos of a finished home: open interior, timber exterior and kitchen"
      points="0,110 230,110 340,0 705,0 445,400 0,400" fill="url(#photoTones)"/>
    <!-- top-left brand corner -->
    <polygon class="brand-corner" points="0,0 350,0 232,118 0,118" fill="var(--black)"/>
    <polygon class="brand-corner__accent" points="0,118 34,118 0,146" fill="var(--green)"/>
    <!-- diagonal bands -->
    <polygon class="band-grey" points="705,0 840,0 570,400 445,400" fill="var(--band-grey)"/>
    <polygon class="band-paper" points="840,0 1200,0 1200,400 570,400" fill="var(--paper)"/>
    <polygon class="band-green-line" points="700,0 716,0 540,195 524,195" fill="var(--green)"/>
    <polygon class="band-dark" points="560,190 640,190 470,400 400,400" fill="var(--black)" opacity="0.35"/>
    <!-- portrait diamond -->
    <polygon class="portrait-frame" points="390,30 555,195 390,360 225,195" fill="var(--frame-white)"/>
    <polygon class="portrait" role="img" aria-label="Team member portrait" points="390,52 533,195 390,338 247,195" fill="var(--photo-grey)"/>
    <!-- accent squares -->
    <polygon points="538,45 549,56 538,67 527,56" fill="var(--green)"/>
    <polygon points="540,90 568,118 540,146 512,118" fill="var(--frame-white)"/>
    <polygon points="244,246 270,272 244,298 218,272" fill="var(--frame-white)"/>
    <polygon points="258,314 278,334 258,354 238,334" fill="var(--green)"/>
    <polygon points="297,298 307,308 297,318 287,308" fill="var(--green)"/>
    <!-- name & role bars -->
    <polygon class="name-bar" points="668,66 1138,66 1138,125 630,125" fill="var(--black)"/>
    <polygon class="role-bar" points="628,133 1138,133 1138,190 586,190" fill="var(--green)"/>
    <!-- footer band -->
    <polygon class="footer-accent" points="630,318 880,318 876,326 626,326" fill="var(--green)"/>
    <polygon class="footer-band" points="600,325 1200,325 1200,400 555,400" fill="var(--black)"/>
  </svg>

  <div class="brand"><span class="brand__mark"></span><span>TLM BESPOKE HOMES</span></div>
  <div class="portrait-label">Photo</div>

  <h1 class="person-name">YOUR NAME</h1>
  <p class="person-role">PROJECT MANAGER</p>

  <div class="contact contact--phone">
    <svg class="contact__icon" viewBox="0 0 42 42" aria-hidden="true">
      <circle cx="21" cy="21" r="21" fill="var(--green)"/>
      <path d="M14 12c1-1 2-1 3 0l2 3c.6 1 .3 1.8-.4 2.4l-1 .9c1 2.4 2.8 4.3 5.2 5.3l.9-1c.6-.7 1.5-1 2.4-.4l3 2c1 .8 1 2 0 3l-1.5 1.4c-1 1-3 1.2-5 .2-4.4-2.2-7.6-5.4-9.7-9.8-1-2-.8-4 .2-5z" fill="none" stroke="#fff" stroke-width="1.8" stroke-linejoin="round"/>
      <path d="M24 12a6 6 0 0 1 6 6M24 15.5a2.5 2.5 0 0 1 2.5 2.5" fill="none" stroke="#fff" stroke-width="1.6" stroke-linecap="round"/>
    </svg>
    <span>1234 567 89</span>
  </div>

  <div class="contact contact--email">
    <svg class="contact__icon" viewBox="0 0 42 42" aria-hidden="true">
      <circle cx="21" cy="21" r="21" fill="var(--green)"/>
      <rect x="11" y="14" width="20" height="14" rx="1.5" fill="none" stroke="#fff" stroke-width="1.8"/>
      <path d="M11.5 15l9.5 7.5 9.5-7.5M11.5 27.5l7-6M30.5 27.5l-7-6" fill="none" stroke="#fff" stroke-width="1.6" stroke-linejoin="round"/>
    </svg>
    <span>yourmail.com</span>
  </div>

  <div class="website">www.tlmbespokehomes.com.au</div>
</div>
</body>
</html>
```